A website design for a consultation firm

We are located in Istanbul, Turkey and offers our consultation services to customers interested in investing in Realestate, Education and Investment particularly this coming from Arab world and English speaking countries.

The site should carry our message of deep knowledge about the Turkish markets in the mentioned sectors of interest, sincerity and keenness.

The final deliverable of the winning design should include:
- The source files of the final designs. e.g. AI, PSD ..etc
- The redline markup for the design using a Specctr or any other similar tool.

Target Market(s)

English and Arabic speaking countries with a Turkish theme since we are a Turkish company

Industry/Entity Type

Consulting

Number of Pages Required

2 page

Font styles to use
Sans Serif

Requirements
Must have
• The site should serve the following main sections:
• - Why QVD?
• - Reports & studies
• - Sectors
• - Our team
• - Contact
• We need a design that could be converted into a WordPress theme.
• The design should be in English but should accommodate other languages including RTL.
• You can use the color theme you like as long as it does't dissolve the logo.
• The site should link into our accounts on the following networks:
• - Twitter
• - Facebook
• - LinkedIn
• The design should be responsive and nicely rendered on Desktop, Tablets and Smart phones.
Nice to have
• The site would be nice to balance between being informative and

```html
<!DOCTYPE html>
<html lang="en">
<head>
<meta charset="utf-8">
<title>QVD Consulting</title>
<link rel="stylesheet" href="https://fonts.googleapis.com/css2?family=Montserrat:wght@400;500;600;700&family=Open+Sans:wght@400;600&display=swap">
<style>
:root{
  --red:#e3132b;
  --navy:#1c2d5e;
  --ink:#2a2f3a;
  --muted:#8a909c;
  --line:#e3e6ec;
  --paper:#ffffff;
  --mist:#f3f4f7;
  --sky:#eef2f7;
}
*{box-sizing:border-box;margin:0;padding:0}
html,body{width:1200px;height:2672px;overflow:hidden}
body{background:var(--paper);font-family:"Open Sans",Arial,sans-serif;color:var(--ink);font-size:13px;line-height:1.55}
h1,h2,h3,h4,.nav,.btn,.brand{font-family:"Montserrat",Arial,sans-serif}
a{color:inherit;text-decoration:none}

/* top bar */
.topbar{height:32px;background:var(--mist);display:flex;align-items:center;justify-content:flex-end;padding-right:40px;gap:0}
.topbar .nav{display:flex;gap:30px;font-size:11px;color:#5a6070;margin-right:40px}
.search{background:var(--red);color:#fff;height:32px;width:180px;display:flex;align-items:center;justify-content:space-between;padding:0 14px;font-size:11px}

/* header */
.header{height:80px;display:flex;align-items:center;justify-content:space-between;padding:0 56px}
.brand{display:flex;align-items:center;gap:10px;font-weight:700;color:var(--navy);font-size:28px;letter-spacing:1px}
.brand .dot{width:26px;height:26px;border-radius:50%;background:var(--red)}
.brand small{display:block;font-size:10px;font-weight:500;letter-spacing:1px;color:var(--navy);margin-top:-4px}
.contacts{display:flex;gap:40px}
.contact{display:flex;align-items:center;gap:10px;font-size:11px}
.contact span{display:block;color:var(--muted);font-size:10px}
.contact b{font-family:"Montserrat",sans-serif;font-weight:600;font-size:13px;color:var(--ink)}

/* hero */
.hero{position:relative;height:496px;background:linear-gradient(90deg,#e9eef4 0%,#c9d2dd 40%,#7c8796 70%,#3d4656 100%)}
.hero-copy{position:absolute;left:56px;top:160px;width:300px}
.hero-copy h4{font-weight:500;color:var(--navy);font-size:26px;line-height:1}
.hero-copy h1{font-weight:600;color:var(--navy);font-size:44px;line-height:1.1;margin-bottom:14px}
.hero-copy p{font-size:12px;color:#4a5060;margin-bottom:22px}
.btn{display:inline-flex;align-items:center;gap:8px;height:34px;padding:0 22px;border-radius:17px;font-size:11px;font-weight:600;color:#fff;background:var(--red)}
.btn.navy{background:var(--navy)}

/* why */
.why{height:352px;background:var(--mist);text-align:center;padding-top:60px}
.title{font-size:34px;font-weight:600;color:var(--navy);letter-spacing:1px}
.title-bar{width:40px;height:3px;background:var(--red);margin:8px auto 0}
.cards{display:flex;justify-content:center;gap:20px;margin-top:44px}
.card{width:300px;height:180px;background:#fff;text-align:left;padding:24px 22px;box-shadow:0 2px 10px rgba(0,0,0,.05)}
.card h3{display:flex;align-items:center;gap:10px;font-size:15px;font-weight:500;color:var(--navy);margin-bottom:10px}
.card p{font-size:11px;color:var(--muted);margin-bottom:12px}
.card a{font-size:10px;font-weight:600;color:var(--navy)}

/* reports */
.reports{position:relative;height:500px;background:#fff;overflow:hidden}
.reports svg.frame{position:absolute;left:0;top:0}
.rs-col{position:absolute;top:170px;width:360px}
.rs-col h2{font-size:30px;font-weight:600;line-height:1.1;margin-bottom:8px}
.rs-col h4{font-size:13px;font-weight:600;margin-bottom:8px}
.rs-col p{font-size:11px;color:var(--muted);margin-bottom:20px}
.rs-left{left:124px}
.rs-left h2{color:var(--red)}
.rs-right{right:124px;text-align:right}
.rs-right h2{color:var(--navy)}
.rs-center{position:absolute;left:540px;top:140px;width:120px;text-align:center}
.rs-center .brand{justify-content:center;font-size:24px}
.amp{display:block;margin-top:60px;font-family:"Montserrat",sans-serif;font-size:28px;color:var(--muted)}

/* sectors */
.sectors{position:relative;height:600px;background:linear-gradient(90deg,#f1f4f8 0%,#f1f4f8 40%,#dfe5ee 100%)}
.sectors-photo{position:absolute;right:0;top:0;width:720px;height:600px;background:linear-gradient(110deg,rgba(241,244,248,1) 0%,#c3ccd8 25%,#6d7a8e 60%,#2f3a52 100%)}
.sectors-copy{position:absolute;left:124px;top:108px;width:360px}
.sectors-copy h2{font-size:46px;font-weight:600;color:var(--navy);line-height:1.1}
.sectors-copy h4{font-size:13px;font-weight:600;color:var(--navy);margin:6px 0 8px}
.sectors-copy p{font-size:11px;color:var(--muted);margin-bottom:28px}
.chips{display:grid;grid-template-columns:150px 150px;gap:10px 16px;margin-bottom:34px}
.chip{height:30px;border:1px solid var(--line);background:#fff;border-radius:15px;display:flex;align-items:center;gap:8px;padding:0 12px;font-size:10px;color:#5a6070}
.chip.on{background:var(--red);border-color:var(--red);color:#fff}

/* team */
.team{height:500px;text-align:center;padding-top:52px;background:#fff}
.team .title{font-weight:500;font-size:36px;color:var(--ink)}
.team .lead{font-size:11px;color:var(--muted);width:340px;margin:10px auto 0}
.members{display:flex;justify-content:center;gap:40px;margin-top:48px}
.member{width:160px}
.avatar{width:160px;height:160px;border-radius:50%;border:5px solid #fff;box-shadow:0 4px 14px rgba(0,0,0,.15)}
.member h3{font-size:13px;font-weight:500;margin-top:20px}
.member span{font-size:10px;color:var(--muted)}

/* footer */
.footer{position:relative;height:112px;background:var(--navy);overflow:hidden}
.footer .white{position:absolute;left:0;top:0}
.footer .brand{position:absolute;left:56px;top:30px}
.footer .nav{position:absolute;left:600px;top:26px;display:flex;gap:34px;font-size:11px;color:#fff}
.social{position:absolute;right:56px;top:56px;display:flex;gap:10px}
.social i{width:14px;height:14px;border-radius:50%;background:#fff;opacity:.85}
.copy{position:absolute;right:56px;top:80px;font-size:9px;color:#aab3c9}
</style>
</head>
<body>

<div class="topbar">
  <nav class="nav"><a>Home</a><a>Why QVD?</a><a>Reports &amp; Studies</a><a>Sectors</a><a>Our team</a><a>Contact</a></nav>
  <div class="search">Search Here
    <svg width="12" height="12" viewBox="0 0 12 12"><circle cx="5" cy="5" r="3.8" fill="none" stroke="#fff" stroke-width="1.4"/><line x1="8" y1="8" x2="11" y2="11" stroke="#fff" stroke-width="1.4"/></svg>
  </div>
</div>

<header class="header">
  <div class="brand"><i class="dot"></i><div>QVD<small>consulting</small></div></div>
  <div class="contacts">
    <div class="contact">
      <svg width="16" height="22" viewBox="0 0 16 22"><rect x="1" y="1" width="14" height="20" rx="2" fill="none" stroke="#2a2f3a" stroke-width="1.6"/><line x1="6" y1="17.5" x2="10" y2="17.5" stroke="#2a2f3a" stroke-width="1.6"/></svg>
      <div><span>Call Us Now</span><b>310-555-0147</b></div>
    </div>
    <div class="contact">
      <svg width="22" height="16" viewBox="0 0 22 16"><rect x="1" y="1" width="20" height="14" rx="1.5" fill="none" stroke="#2a2f3a" stroke-width="1.6"/><polyline points="1,2 11,9 21,2" fill="none" stroke="#2a2f3a" stroke-width="1.6"/></svg>
      <div><span>Email Address</span><b>hello@qvd-advisory.com</b></div>
    </div>
  </div>
</header>

<section class="hero" role="img" aria-label="Photo of two business consultants in suits smiling at a meeting table">
  <div class="hero-copy">
    <h4>hello</h4>
    <h1>consulting</h1>
    <p>We guide investors through Turkish markets with clear advice, local insight and honest support at every step.</p>
    <a class="btn">Read More</a>
  </div>
</section>

<section class="why">
  <h2 class="title">Why QVD?</h2>
  <div class="title-bar"></div>
  <div class="cards">
    <article class="card">
      <h3><svg width="22" height="20" viewBox="0 0 22 20"><rect x="2" y="6" width="18" height="13" fill="none" stroke="#8a909c" stroke-width="1.5"/><polyline points="1,7 11,1 21,7" fill="none" stroke="#8a909c" stroke-width="1.5"/></svg>Realestate</h3>
      <p>Trusted guidance on buying homes and commercial property across Istanbul and beyond, from search to title deed.</p>
      <a>Read More ›</a>
    </article>
    <article class="card">
      <h3><svg width="22" height="20" viewBox="0 0 22 20"><rect x="2" y="3" width="18" height="14" fill="none" stroke="#8a909c" stroke-width="1.5"/><line x1="11" y1="3" x2="11" y2="17" stroke="#8a909c" stroke-width="1.5"/></svg>Education</h3>
      <p>Support for students and families choosing Turkish schools and universities, with help on every admission step.</p>
      <a>Read More ›</a>
    </article>
    <article class="card">
      <h3><svg width="22" height="20" viewBox="0 0 22 20"><circle cx="11" cy="10" r="8.5" fill="none" stroke="#8a909c" stroke-width="1.5"/><ellipse cx="11" cy="10" rx="4" ry="8.5" fill="none" stroke="#8a909c" stroke-width="1.5"/><line x1="2.5" y1="10" x2="19.5" y2="10" stroke="#8a909c" stroke-width="1.5"/></svg>English speaking countries</h3>
      <p>Dedicated advisers for clients from English and Arabic speaking countries, in your own language.</p>
      <a>Read More ›</a>
    </article>
  </div>
</section>

<section class="reports">
  <svg class="frame" width="1200" height="500" viewBox="0 0 1200 500">
    <defs>
      <linearGradient id="fade" x1="0" x2="1"><stop offset="0" stop-color="#eef1f6" stop-opacity="0"/><stop offset=".5" stop-color="#eef1f6"/><stop offset="1" stop-color="#eef1f6" stop-opacity="0"/></linearGradient>
    </defs>
    <polygon points="600,10 1000,250 600,490 200,250" fill="url(#fade)"/>
    <polygon points="600,10 1000,250 600,490 200,250" fill="none" stroke="#dfe3ea" stroke-width="1"/>
  </svg>
  <div class="rs-col rs-left">
    <h2>Reports</h2>
    <h4>Market reports available</h4>
    <p>Quarterly reports on Turkish property prices, rental yields and demand by district, written for foreign investors who need clear numbers before they commit capital.</p>
    <a class="btn">Read More ›</a>
  </div>
  <div class="rs-center">
    <div class="brand"><i class="dot"></i>QVD</div>
    <span class="amp">&amp;</span>
  </div>
  <div class="rs-col rs-right">
    <h2>Studies</h2>
    <h4>In depth sector studies</h4>
    <p>Detailed studies on education, real estate and investment trends in Turkey, drawn from local research, official data and years of field work with our clients.</p>
    <a class="btn navy">Read More ›</a>
  </div>
</section>

<section class="sectors">
  <div class="sectors-photo" role="img" aria-label="Photo of consultants reviewing documents together at a desk"></div>
  <div class="sectors-copy">
    <h2>Sectors</h2>
    <h4>Advice in the sectors that matter most</h4>
    <p>We focus on a few sectors and know them deeply, so every client gets sound, tested advice on where and how to invest.</p>
    <div class="chips">
      <span class="chip"><svg width="10" height="10" viewBox="0 0 10 10"><polyline points="1,5 4,8 9,2" fill="none" stroke="currentColor" stroke-width="1.5"/></svg>Real estate</span>
      <span class="chip"><svg width="10" height="10" viewBox="0 0 10 10"><polyline points="1,5 4,8 9,2" fill="none" stroke="currentColor" stroke-width="1.5"/></svg>Education</span>
      <span class="chip"><svg width="10" height="10" viewBox="0 0 10 10"><polyline points="1,5 4,8 9,2" fill="none" stroke="currentColor" stroke-width="1.5"/></svg>Investment</span>
      <span class="chip on"><svg width="10" height="10" viewBox="0 0 10 10"><polyline points="1,5 4,8 9,2" fill="none" stroke="currentColor" stroke-width="1.5"/></svg>Residency</span>
      <span class="chip"><svg width="10" height="10" viewBox="0 0 10 10"><polyline points="1,5 4,8 9,2" fill="none" stroke="currentColor" stroke-width="1.5"/></svg>Tourism</span>
      <span class="chip"><svg width="10" height="10" viewBox="0 0 10 10"><polyline points="1,5 4,8 9,2" fill="none" stroke="currentColor" stroke-width="1.5"/></svg>Healthcare</span>
    </div>
    <a class="btn navy">Read More</a>
  </div>
</section>

<section class="team">
  <h2 class="title">Our team</h2>
  <p class="lead">Our advisers bring local knowledge, sincerity and care to every client we serve.</p>
  <div class="members">
    <div class="member"><div class="avatar" role="img" aria-label="Portrait of Elena Marsh" style="background:linear-gradient(160deg,#e8c07a,#b07a3e)"></div><h3>Elena Marsh</h3><span>Senior Adviser</span></div>
    <div class="member"><div class="avatar" role="img" aria-label="Portrait of Daniel Okoro" style="background:linear-gradient(160deg,#e7b36a,#9c6a3a)"></div><h3>Daniel Okoro</h3><span>Investment Lead</span></div>
    <div class="member"><div class="avatar" role="img" aria-label="Portrait of Sofia Brandt" style="background:linear-gradient(160deg,#6d8fa8,#3b4a5c)"></div><h3>Sofia Brandt</h3><span>Education Adviser</span></div>
    <div class="member"><div class="avatar" role="img" aria-label="Portrait of Leo Harmon" style="background:linear-gradient(160deg,#d8dde4,#8d97a6)"></div><h3>Leo Harmon</h3><span>Client Relations</span></div>
  </div>
</section>

<footer class="footer">
  <svg class="white" width="560" height="112" viewBox="0 0 560 112"><polygon points="0,0 500,0 460,112 0,112" fill="#fff"/><polygon points="500,0 520,0 480,112 460,112" fill="#e3132b"/></svg>
  <div class="brand"><i class="dot"></i><div>QVD<small>consulting</small></div></div>
  <nav class="nav"><a>Home</a><a>Why QVD</a><a>Reports &amp; Studies</a><a>Sectors</a><a>Our team</a><a>Contact</a></nav>
  <div class="social" aria-label="Social links"><i></i><i></i><i></i></div>
  <div class="copy">Copyright © 2024 QVD Consulting. All rights reserved.</div>
</footer>

</body>
</html>
```